Website design for management consulting firm

We need a web design for a new consulting company based in Boston, MA called "Quillmoor Ridge Consulting." This webpage will be simple home page, with a "contact us" page, that describes the services of the consulting firm. The company provides strategic planning, business assessment, process re-designs, and other management consulting functions. I would like the website to look high-tech. A logo was already created via Artsy Hive.

Target Market(s)

Other business owners across a wide spectrum of industries - from IT to retail.

Industry/Entity Type

It Company

Number of Pages Required

3 page

Colors
0455a3
ffffff

Requirements
Must have
• Front page that provides generic text / overview of the firm. A "services" tab that describes consulting services. A "contact us" tab that provides either a form to contact us or just the contact email address of the company. info@quillmoorridgeconsulting.example

```html
<!DOCTYPE html>
<html lang="en">
<head>
<meta charset="utf-8">
<title>Quillmoor Ridge Consulting</title>
<link rel="stylesheet" href="https://fonts.googleapis.com/css2?family=Raleway:wght@500;600&family=Open+Sans:wght@400;600&display=swap">
<style>
:root{
  --ink:#141414;
  --header:#151617;
  --brand-blue:#0455a3;
  --button-blue:#0b5f8c;
  --title-blue:#0b4d78;
  --teal:#1ea9a0;
  --white:#ffffff;
  --body-grey:#555c63;
  --panel-text:#e4e7ea;
}
*{box-sizing:border-box;margin:0;padding:0}
html,body{width:680px;height:1200px;overflow:hidden;background:var(--white)}
body{position:relative;font-family:"Open Sans",Arial,sans-serif;color:var(--ink)}

.site-header{position:absolute;left:0;top:0;width:680px;height:44px;background:var(--header);z-index:2}
.brand{position:absolute;left:27px;top:0;height:44px;display:flex;align-items:center;gap:8px}
.brand-mark{width:16px;height:16px;background:var(--brand-blue)}
.brand-name{font-family:"Raleway",Arial,sans-serif;font-weight:600;font-size:17px;color:var(--white);letter-spacing:-.2px}
.main-nav a{position:absolute;top:0;display:block;height:44px;line-height:46px;font-size:6.5px;color:var(--white);text-decoration:none;text-transform:uppercase;letter-spacing:.2px}
.main-nav .home{left:422px;width:38px;text-align:center;background:var(--button-blue)}
.main-nav .about{left:485px}
.main-nav .services{left:551px}
.main-nav .contact{left:614px}

.hero{position:absolute;left:0;top:44px;width:680px;height:374px;overflow:hidden;box-shadow:0 4px 8px rgba(0,0,0,.25)}
.hero-photo{position:absolute;inset:0;background:
  radial-gradient(ellipse 120px 190px at 360px 210px,rgba(30,32,36,.75),rgba(30,32,36,0)),
  radial-gradient(ellipse 170px 120px at 200px 330px,rgba(60,45,38,.7),rgba(60,45,38,0)),
  radial-gradient(ellipse 220px 160px at 600px 120px,rgba(150,170,182,.55),rgba(150,170,182,0)),
  radial-gradient(ellipse 200px 150px at 80px 90px,rgba(120,138,150,.5),rgba(120,138,150,0)),
  linear-gradient(180deg,#6c7a83 0%,#56626a 45%,#3a3e42 85%,#2e3033 100%)}
.hero-title{position:absolute;left:0;top:147px;width:680px;text-align:center;font-family:"Raleway",Arial,sans-serif;font-weight:500;font-size:32px;color:var(--white);letter-spacing:.3px}
.hero-rule{position:absolute;left:50px;top:186px;width:580px;height:1px;background:rgba(255,255,255,.45)}
.hero-text{position:absolute;left:120px;top:193px;width:440px;text-align:center;font-size:7.5px;line-height:13px;color:var(--white)}
.hero-button{position:absolute;left:306px;top:241px;width:67px;height:20px;line-height:20px;border-radius:3px;background:var(--button-blue);color:var(--white);font-size:6.5px;text-align:center;text-transform:uppercase}
.slider-arrow{position:absolute;top:177px;width:21px;height:21px}
.slider-arrow.prev{left:27px}
.slider-arrow.next{left:633px}

.welcome{position:absolute;left:0;top:418px;width:680px;height:98px;text-align:center}
.welcome-title{margin-top:26px;font-family:"Raleway",Arial,sans-serif;font-weight:500;font-size:21px;color:var(--title-blue)}
.welcome-title span{color:var(--teal)}
.welcome-text{width:520px;margin:8px auto 0;font-size:7px;line-height:10px;color:var(--body-grey)}

.service-grid{position:absolute;left:0;top:516px;width:680px;height:640px}
.tile{position:absolute;height:160px;overflow:hidden}
.tile.left{left:0;width:343px}
.tile.right{left:343px;width:337px}
.tile-bg{position:absolute;inset:0}
.service-body{position:absolute;top:50px;width:260px}
.left .service-body{left:37px;text-align:left}
.right .service-body{right:27px;text-align:right}
.service-title{font-weight:400;font-size:11px;color:var(--teal);text-transform:uppercase;letter-spacing:.2px}
.service-text{margin-top:5px;font-size:6.6px;line-height:9px;color:var(--panel-text)}
.read-more{display:inline-block;margin-top:8px;width:63px;height:20px;line-height:20px;border-radius:2px;background:var(--white);color:var(--button-blue);font-size:6.5px;text-align:center;text-transform:uppercase}

.site-footer{position:absolute;left:0;top:1156px;width:680px;height:44px;background:var(--ink)}
.copyright{position:absolute;left:0;width:690px;top:0;line-height:44px;text-align:center;font-size:6.5px;color:var(--white)}
.social{position:absolute;right:33px;top:14px;display:flex;gap:6px}
.social span{width:16px;height:16px;border:1px solid #9aa0a4}
.social span.filled{background:var(--teal);border-color:var(--teal)}
</style>
</head>
<body>

<header class="site-header">
  <div class="brand"><span class="brand-mark"></span><span class="brand-name">Quillmoor Ridge Consulting</span></div>
  <nav class="main-nav">
    <a class="home" href="#">Home</a>
    <a class="about" href="#">About Us</a>
    <a class="services" href="#">Services</a>
    <a class="contact" href="#">Contact Us</a>
  </nav>
</header>

<section class="hero">
  <div class="hero-photo" role="img" aria-label="Photo of business people meeting around a table in a bright office"></div>
  <h1 class="hero-title">LET US COOPERATION !</h1>
  <div class="hero-rule"></div>
  <p class="hero-text">Lorem ipsum dolor sit amet, consectetur adipiscing elit, sed do eiusmod tempor incididunt ut labore et dolore magna aliqua. Ut enim ad minim veniam, quis nostrud exercitation ullamco laboris nisi ut aliquip ex ea commodo consequat. Duis aute irure dolor in reprehenderit in voluptate velit esse cillum dolore eu fugiat nulla pariatur.</p>
  <div class="hero-button">Read More</div>
  <svg class="slider-arrow prev" viewBox="0 0 21 21" aria-hidden="true"><circle cx="10.5" cy="10.5" r="10.5" fill="#e9eef2"/><path d="M12 6.5 8 10.5 12 14.5" fill="none" stroke="#0b5f8c" stroke-width="1.8"/></svg>
  <svg class="slider-arrow next" viewBox="0 0 21 21" aria-hidden="true"><circle cx="10.5" cy="10.5" r="10.5" fill="#e9eef2"/><path d="M9 6.5 13 10.5 9 14.5" fill="none" stroke="#0b5f8c" stroke-width="1.8"/></svg>
</section>

<section class="welcome">
  <h2 class="welcome-title">Welcome to <span>Quillmoor Ridge</span></h2>
  <p class="welcome-text">Lorem ipsum dolor sit amet, consectetur adipiscing elit, sed do eiusmod tempor incididunt ut labore et dolore magna aliqua. Ut enim ad minim veniam, quis nostrud exercitation ullamco laboris nisi ut aliquip ex ea commodo consequat.</p>
</section>

<section class="service-grid">
  <div class="tile left" style="top:0">
    <div class="tile-bg" role="img" aria-label="Photo of hands reviewing printed analysis charts on a desk" style="background:
      radial-gradient(ellipse 90px 70px at 60px 100px,rgba(40,90,150,.55),rgba(40,90,150,0)),
      radial-gradient(ellipse 110px 80px at 270px 50px,rgba(70,140,60,.6),rgba(70,140,60,0)),
      radial-gradient(ellipse 120px 70px at 200px 140px,rgba(50,90,150,.55),rgba(50,90,150,0)),
      linear-gradient(135deg,#b79a74 0%,#e4e2dc 40%,#eef0ec 60%,#c8d2b8 100%)"></div>
  </div>
  <div class="tile right" style="top:0">
    <div class="tile-bg" role="img" aria-label="Dimmed photo of financial reports spread on a table" style="background:
      radial-gradient(ellipse 160px 90px at 120px 80px,rgba(95,100,104,.6),rgba(95,100,104,0)),
      linear-gradient(135deg,#45494c,#2c2e30)"></div>
    <div class="service-body">
      <h3 class="service-title">Strategic Planning</h3>
      <p class="service-text">Lorem ipsum dolor sit amet, consectetur adipiscing elit, sed do eiusmod tempor incididunt ut labore et dolore magna aliqua. Ut enim ad minim veniam, quis nostrud exercitation ullamco laborismodo consequat.</p>
      <div class="read-more">Read More</div>
    </div>
  </div>

  <div class="tile left" style="top:160px">
    <div class="tile-bg" role="img" aria-label="Dimmed photo of a laptop keyboard" style="background:
      radial-gradient(ellipse 170px 60px at 200px 130px,rgba(70,66,62,.6),rgba(70,66,62,0)),
      linear-gradient(135deg,#2f2c29,#1c1b1a)"></div>
    <div class="service-body">
      <h3 class="service-title">Business Assessment</h3>
      <p class="service-text">Lorem ipsum dolor sit amet, consectetur adipiscing elit, sed do eiusmod tempor incididunt ut labore et dolore magna aliqua. Ut enim ad minim veniam, quis nostrud exercitation ullamco laborismodo consequat.</p>
      <div class="read-more">Read More</div>
    </div>
  </div>
  <div class="tile right" style="top:160px">
    <div class="tile-bg" role="img" aria-label="Photo of a hand writing in an open notebook on a wooden desk" style="background:
      radial-gradient(ellipse 110px 75px at 180px 100px,rgba(246,242,236,.95),rgba(246,242,236,0)),
      radial-gradient(ellipse 90px 80px at 320px 30px,rgba(70,52,40,.9),rgba(70,52,40,0)),
      linear-gradient(135deg,#b9622a 0%,#cc7f42 50%,#b56a34 100%)"></div>
  </div>

  <div class="tile left" style="top:320px">
    <div class="tile-bg" role="img" aria-label="Photo of cars crossing a green steel bridge" style="background:
      radial-gradient(ellipse 90px 40px at 150px 105px,rgba(40,70,160,.55),rgba(40,70,160,0)),
      linear-gradient(180deg,#e4e8e9 0%,#7fa597 25%,#3f7563 45%,#858a8e 65%,#6b6e71 100%)"></div>
  </div>
  <div class="tile right" style="top:320px">
    <div class="tile-bg" role="img" aria-label="Dimmed photo of bridge traffic" style="background:
      radial-gradient(ellipse 170px 60px at 100px 30px,rgba(70,88,84,.6),rgba(70,88,84,0)),
      linear-gradient(135deg,#3b3f41,#26282a)"></div>
    <div class="service-body">
      <h3 class="service-title">Process Re-Designs</h3>
      <p class="service-text">Lorem ipsum dolor sit amet, consectetur adipiscing elit, sed do eiusmod tempor incididunt ut labore et dolore magna aliqua. Ut enim ad minim veniam, quis nostrud exercitation ullamco laborismodo consequat.</p>
      <div class="read-more">Read More</div>
    </div>
  </div>

  <div class="tile left" style="top:480px">
    <div class="tile-bg" role="img" aria-label="Dimmed photo of a business presentation" style="background:
      radial-gradient(ellipse 90px 70px at 70px 40px,rgba(40,70,64,.55),rgba(40,70,64,0)),
      radial-gradient(ellipse 90px 80px at 280px 60px,rgba(70,64,58,.5),rgba(70,64,58,0)),
      linear-gradient(135deg,#2e2f30,#1c1d1e)"></div>
    <div class="service-body">
      <h3 class="service-title">Management Consulting</h3>
      <p class="service-text">In the centuries since Marcus Veridan led a Roman legion across the Rubicon River, “crossing the Rubicon” has become synonymous with irrevocably committing oneself to a bold and revolutionary course of action.</p>
      <div class="read-more">Read More</div>
    </div>
  </div>
  <div class="tile right" style="top:480px">
    <div class="tile-bg" role="img" aria-label="Photo of a presenter beside a rising growth chart on a whiteboard" style="background:
      radial-gradient(ellipse 60px 90px at 250px 90px,rgba(40,44,60,.35),rgba(40,44,60,0)),
      radial-gradient(ellipse 120px 60px at 120px 90px,rgba(232,160,160,.5),rgba(232,160,160,0)),
      linear-gradient(135deg,#f4f4f5 0%,#f0e2e2 50%,#e9ecef 100%)"></div>
  </div>
</section>

<footer class="site-footer">
  <p class="copyright">Copyright 2015 Company Name All Rights Reserved.</p>
  <div class="social" aria-label="Social links">
    <span></span><span></span><span class="filled"></span><span></span>
  </div>
</footer>

</body>
</html>
```